Article/Flyer - Reservation of Rights

We would like an article that we normally produce through illustrator in a pdf format to be placed in a Word format. We have provided a sample article/flyer of our normal distribution style. We would like the outcome to be in WORD format

```html
<!DOCTYPE html>
<html lang="en">
<head>
<meta charset="utf-8">
<title>Reservation of Rights Letter – Brightwater Insurance</title>
<link rel="stylesheet" href="https://fonts.googleapis.com/css2?family=Carlito:wght@400;700&family=Arimo:wght@700&family=Cormorant+Garamond:wght@500&family=Cabin:wght@400&display=swap">
<style>
  :root{
    --backdrop:#e9dcc8;
    --paper:#ffffff;
    --ink:#1f1f1f;
    --accent:#8b1e2b;
    --brand-ink:#3a2a2e;
    --slate:#6f8ea3;
    --sky:#cfe0f0;
    --sky-deep:#a9c6e2;
  }
  *{box-sizing:border-box;margin:0;padding:0}
  html,body{width:1200px;height:960px;overflow:hidden}
  body{background:var(--backdrop);position:relative;font-family:"Carlito","Calibri",sans-serif;color:var(--ink)}
  .page{position:absolute;top:128px;width:552px;height:714px;background:var(--paper);box-shadow:0 2px 6px rgba(0,0,0,.18)}
  .page--front{left:25px}
  .page--back{left:613px}
  .abs{position:absolute}

  .masthead{left:37px;top:32px;width:487px;height:167px;
    background:linear-gradient(100deg,#dfeaf3 0%,#b7cbdd 35%,#c9c3cf 60%,#9fb3c4 80%,#d8e2ea 100%)}
  .brand{position:absolute;left:42px;top:20px;font-family:"Carlito","Calibri",sans-serif;color:var(--brand-ink)}
  .brand__name{font-weight:700;font-size:26px;line-height:1}
  .brand__tag{font-weight:700;font-size:9px;margin-top:5px}

  .rule{height:1.5px;background:var(--accent);left:37px;width:487px}
  .intro{left:37px;top:213px;width:487px;font-size:10.8px;line-height:15.4px}
  .intro strong{font-family:"Arimo",sans-serif;font-size:10px;color:var(--accent)}

  .col{width:234px;font-size:9.6px;line-height:17.1px}
  .col p{margin-bottom:10px}
  .col h2{font-family:"Arimo",sans-serif;font-weight:700;font-size:9.8px;color:var(--accent);line-height:14px;margin-bottom:2px}

  .plan-photo{left:33px;top:35px;width:235px;height:158px;
    background:linear-gradient(135deg,#f2f2f0 0%,#dcdcd8 45%,#8c8f95 70%,#e6e6e3 100%)}

  .promo{left:33px;width:487px}
  .promo__lead{top:426px;height:83px;background:var(--slate);color:#fff;font-family:"Cabin",sans-serif;font-size:20.5px;line-height:24px;text-align:center;padding-top:6px}
  .promo__cta{top:514px;left:32px;width:488px;height:40px;background:var(--accent);color:#fff;font-family:"Cabin",sans-serif;font-size:20.5px;line-height:40px;text-align:center}
  .promo__contact{top:554px;height:129px;background:linear-gradient(180deg,var(--sky) 0%,#e3edf7 50%,var(--sky-deep) 100%)}
  .office-photo{left:97px;top:562px;width:152px;height:108px;
    background:linear-gradient(180deg,#5b6f88 0%,#8b3a3a 55%,#3c3f48 100%)}
  .links{left:280px;top:564px;font-family:"Cormorant Garamond",serif;font-weight:500;font-size:16px;color:#2a2a2a;line-height:1}
  .links li{list-style:none;display:flex;align-items:center;height:16px}
  .links li + li{margin-top:10px}
  .links .mark{width:15px;height:15px;background:var(--slate);margin-right:8px;flex:none}
</style>
</head>
<body>

<article class="page page--front">
  <header class="abs masthead" role="img" aria-label="Photo of a city office tower and three design professionals reviewing plans">
    <div class="brand">
      <div class="brand__name">Brightwater Insurance</div>
      <div class="brand__tag">Serving Architects, Engineers and Environmental Consultants</div>
    </div>
  </header>
  <div class="abs rule" style="top:202px"></div>
  <p class="abs intro">Reporting a claim or potential claim to your professional liability insurance company will trigger a fair amount of return correspondence that often creates confusion rather than clarity.&nbsp; One document that commonly falls into this category is the <strong>Reservation of Rights Letter</strong>.</p>
  <div class="abs rule" style="top:259px"></div>

  <section class="abs col" style="left:37px;top:277px">
    <h2>What is the Reservation of Rights Letter</h2>
    <p>The Reservation of Rights Letter is a normal part of the insurance claims process. Its purpose is to provide notification from the insurance company to the policy holder that coverage may not apply.&nbsp; While this often comes as alarming news, the Reservation of Rights Letter should not be mistaken as an outright denial—it does not automatically mean that coverage is being or will be denied.</p>
    <p>This standard correspondence is routinely sent to comply with state laws and preserve the insurance company’s legal ability to deny some, or all, of the claim pending further investigation while the claim is ongoing and being handled by the insurance company.&nbsp; Failure to send the letter could be considered a waiver of their rights at a later time.</p>
    <p>Because information is vague in the early stages of a claim and often is limited to unsubstantiated allegations and a few facts, the Reservation of Rights Letter protects the insurance company’s interests to later deny coverage in whole or part based on evidence revealed during claims handling.</p>
  </section>

  <section class="abs col" style="left:285px;top:277px;width:238px">
    <h2>Interpreting the Letter</h2>
    <p>Most of the time the Reservation of Rights Letter is a generic&nbsp; form letter that states your insurance company is proceeding with handling your claim but reserves the right to deny coverage later on based upon any information that reveals reason to deny.</p>
    <p>Legitimate reasons an insurance company may deny coverage include when the loss occurred in relation to your retroactive date, specific exclusions in the policy language, prior knowledge of the incident, and coverage by another policy, among others.</p>
    <p>If the insurance company believes there may be reason for denial at the time the Reservation of Rights Letter is sent, it will be stated in the letter.&nbsp; For example, if the claim alleges breach of warranty, the letter will state that warranties are specifically excluded by the policy and it will include the policy language to demonstrate the exclusion.</p>
    <p>Even when specific reasons for potential coverage denial are cited, it is important to note that this is not a final verdict nor does it mean complete lack of cover-age. Generally the insurance company is obligated to help you</p>
  </section>
</article>

<article class="page page--back">
  <div class="abs plan-photo" role="img" aria-label="Photo of architectural blueprints with pencils and a ruler"></div>

  <section class="abs col" style="left:33px;top:211px;width:238px">
    <p>if any of your claims are covered by your insurance policy — there is a duty to defend.&nbsp; In cases such as the scenario above, circumstances of the claim will influence what is covered and what may be subject to exclusion.</p>
    <p>Based on investigative conclusions, the insurance company may not be obligated to pay the damages for certain types or aspects of claims.</p>
  </section>

  <section class="abs col" style="left:279px;top:45px;width:244px">
    <h2>How to Proceed</h2>
    <p>Although the intent of the Reservation of Rights Letter is to protect the insurance company’s interests, it also alerts the policy holder to the fact that some elements of a claim may not be covered and therefore allows the insured to take steps to protect its potentially uninsured interests.</p>
    <p>However, receiving the Reservation of Rights Letter and even the insurance company’s interpretation of the policy language or law that they believe points toward coverage declination does not mean that you are automatically required to accept a denial of coverage.</p>
    <p>The best thing to do upon receiving the letter is to contact your broker and work closely with them and the insurance company claims handling department to ensure the prompt and fair handling of your claim.</p>
  </section>

  <div class="abs promo promo__lead">An insurance agent who has experience<br>with large Top 100 firms as well as<br>small design firms.</div>
  <div class="abs promo__cta">Connect with Brightwater Insurance</div>
  <div class="abs promo promo__contact"></div>
  <div class="abs office-photo" role="img" aria-label="Photo of the company office building at dusk"></div>
  <ul class="abs links">
    <li>www.brightwaterins.com</li>
    <li><span class="mark"></span>/BrightwaterIns</li>
    <li><span class="mark"></span>/BrightwaterGroup</li>
    <li><span class="mark"></span>/BrightwaterIns</li>
  </ul>
</article>

</body>
</html>
```